Brand refresh of quote, work docket and Fire certificate documents

I would like a refresh of our document suit including

1. Front page called VOLT3 Proposal
2. Quote document template
3. Work docket template
4. Fire certificate template - to look like a professional complaint certificate

Examples of documents are attached.

```html
<!DOCTYPE html>
<html lang="en">
<head>
<meta charset="utf-8">
<title>VOLT3 Document Suite</title>
<link href="https://fonts.googleapis.com/css2?family=Oswald:wght@500;600;700&family=Montserrat:wght@400;500;600;700;800&family=Source+Sans+3:wght@400;600;700&display=swap" rel="stylesheet">
<style>
:root{
  --bg:#e6e6e6;
  --orange:#f47c20;
  --ink:#1f1f1f;
  --grey:#3a3a3a;
  --panel:#f1f1f2;
  --rule:#c9c9cc;
  --red:#e5322d;
  --white:#ffffff;
}
*{box-sizing:border-box;margin:0;padding:0}
html,body{width:1200px;height:1200px;overflow:hidden;background:var(--bg)}
body{position:relative;font-family:"Montserrat",sans-serif;color:var(--ink)}
.page{position:absolute;width:396px;height:511px;background:var(--white);box-shadow:0 6px 18px rgba(0,0,0,.22);overflow:hidden}
.page--cover{left:192px;top:78px}
.page--quote{left:612px;top:78px}
.page--docket{left:192px;top:612px}
.page--cert{left:612px;top:612px}
.abs{position:absolute}

/* cover */
.cover-photo{position:absolute;inset:0;background:radial-gradient(ellipse at 65% 30%,#6b5a55 0%,#3b2520 40%,#2a1410 70%),linear-gradient(180deg,#3a2a28,#5a1e12);}
.cover-photo::after{content:"";position:absolute;inset:0;background:linear-gradient(180deg,rgba(0,0,0,0) 35%,rgba(110,30,10,.55) 100%)}
.cover-tab{position:absolute;left:0;top:0;width:200px;height:86px;background:var(--white);clip-path:polygon(0 0,100% 0,84% 88%,76% 100%,0 100%)}
.brand{position:absolute;font-family:"Montserrat",sans-serif;font-weight:800;letter-spacing:-1px;line-height:1}
.brand-mark{display:inline-block;width:7px;height:7px;border-radius:50%;background:var(--orange);margin-right:4px;vertical-align:middle}
.tagline{position:absolute;font-size:6.4px;letter-spacing:2.4px;font-weight:500}
.cover-title{position:absolute;left:30px;font-family:"Oswald",sans-serif;line-height:1}
.cover-title--brand{top:258px;font-size:104px;font-weight:600;color:var(--orange);letter-spacing:-1px}
.cover-title--doc{top:358px;font-size:58px;font-weight:600;color:var(--white)}
.cover-sub{position:absolute;left:28px;top:432px;font-family:"Oswald",sans-serif;font-size:23.5px;font-weight:500;color:var(--white);letter-spacing:.2px}
.cover-url{position:absolute;left:0;width:100%;top:482px;text-align:center;font-size:9.5px;font-weight:600;color:var(--white)}
.cover-bar{position:absolute;left:0;bottom:0;width:100%;height:11px;background:var(--orange)}

/* shared header/footer */
.header{position:absolute;left:0;top:0;width:100%;height:80px;background:linear-gradient(90deg,#7a2a14 0%,#b8481c 45%,#9a3a18 70%,#6e2410 100%)}
.header .brand{left:32px;top:30px;font-size:28px;color:var(--white)}
.header .tagline{left:32px;top:60px;font-size:4.6px;letter-spacing:2.2px;color:#f3d6c4}
.company{position:absolute;right:32px;top:15px;text-align:right;color:var(--white);font-size:6.6px;line-height:1.2}
.company strong{display:block;font-size:9px;font-weight:700;margin-bottom:4px}
.footer{position:absolute;left:0;bottom:0;width:100%;height:16px;background:var(--orange);color:var(--white);font-size:5.5px;font-weight:600;text-align:center;line-height:16px}

/* quote */
.q-head{position:absolute;left:24px;top:121px;width:347px;height:21px;border-radius:6px;background:var(--orange);color:var(--white);font-size:9px;font-weight:600;letter-spacing:.5px}
.q-head span,.q-row span{position:absolute;top:50%;transform:translateY(-50%)}
.q-body{position:absolute;left:24px;top:150px;width:347px;height:167px;border-radius:7px;background:var(--panel)}
.q-row{position:absolute;left:0;width:100%;height:40px;font-size:8px;letter-spacing:.4px;color:var(--grey)}
.q-row::after{content:"";position:absolute;left:0;right:9px;bottom:0;height:1px;background:var(--rule)}
.c-sl{left:9px}.c-desc{left:36px}.c-price{left:198px}.c-qty{left:254px}.c-total{left:294px}
.q-thanks{left:33px;top:350px;font-size:7px;font-weight:700;letter-spacing:.3px}
.q-pay{left:33px;top:375px;font-size:7.5px;font-weight:600;color:var(--orange)}
.q-paylist{left:33px;top:387px;font-size:4.4px;font-weight:600;line-height:1.65;display:grid;grid-template-columns:44px auto}
.q-sum{left:262px;top:349px;font-size:7px;font-weight:700;display:grid;grid-template-columns:67px auto;row-gap:6px;letter-spacing:.3px}
.q-total{left:262px;top:387px;font-size:9.5px;font-weight:600;color:var(--orange);display:grid;grid-template-columns:60px auto;letter-spacing:.4px}
.q-line{left:33px;top:425px;width:74px;height:1px;background:var(--grey)}
.q-terms{left:33px;top:435px;font-size:6.5px;font-weight:600;color:var(--orange);letter-spacing:.3px}
.q-terms-text{left:33px;top:446px;width:160px;font-size:3.9px;font-weight:600;line-height:1.6}
.q-sign{left:281px;top:455px;width:74px;border-top:1px solid var(--grey);padding-top:4px;font-size:6px;font-weight:600;text-align:center;letter-spacing:.3px}

/* docket */
.d-pill{position:absolute;left:117px;top:96px;width:161px;height:24px;border-radius:8px;background:var(--orange);color:var(--white);font-size:16px;font-weight:600;text-align:center;line-height:24px}
.d-rule{position:absolute;top:125px;height:1px;background:var(--orange)}
.d-client{left:32px;top:148px;font-size:9.5px;font-weight:700}
.d-date{left:157px;top:146px;font-size:8px}
.d-addr{left:32px;top:162px;font-size:6px}
.d-contact{left:32px;top:174px;font-size:9.5px;font-weight:700}
.d-info{position:absolute;left:19px;top:201px;width:357px;height:35px;border-radius:6px;background:var(--panel);padding:7px 13px}
.d-info b{display:block;font-size:7.4px;font-weight:600;margin-bottom:6px}
.d-info p{font-size:5px}
.d-works{position:absolute;left:19px;top:262px;width:357px;height:217px;border-radius:7px;background:var(--panel)}
.d-works-pill{position:absolute;left:25px;top:252px;padding:0 7px;height:19px;border-radius:5px;background:var(--orange);color:var(--white);font-size:12px;font-weight:600;line-height:19px}
.d-item{position:absolute;left:32px;font-size:8px;font-weight:600;line-height:1.1}
.d-item small{display:block;font-size:5px;font-weight:400}

/* certificate */
.cert{font-family:"Source Sans 3",sans-serif;font-size:9px;color:var(--ink)}
.cert .label{font-weight:700}
.cert-field{position:absolute;left:33px;display:flex}
.cert-field .label{width:52px}
.cert-para{position:absolute;left:33px;width:320px;line-height:1.5}
.cert-num{color:var(--red);font-weight:700}
.sig{display:inline-block;width:58px;height:22px;vertical-align:middle;margin-left:8px;background:linear-gradient(90deg,#f2f2f2,#e4e4e4);border-radius:3px}
</style>
</head>
<body>

<!-- Proposal cover -->
<section class="page page--cover">
  <div class="cover-photo" role="img" aria-label="Photo of a firefighter in a red helmet and breathing apparatus beside a fire truck"></div>
  <div class="cover-tab"></div>
  <div class="brand" style="left:26px;top:28px;font-size:38px;color:var(--grey)"><span class="brand-mark"></span>VOLT3</div>
  <div class="tagline" style="left:27px;top:70px;color:var(--grey)">PASSIVE FIRE PROTECTION</div>
  <div class="cover-title cover-title--brand">VOLT3</div>
  <div class="cover-title cover-title--doc">PROPOSAL</div>
  <div class="cover-sub">PASSIVE FIRE PROTECTION SPECIALISTS</div>
  <div class="cover-url">www.volt3.com.au</div>
  <div class="cover-bar"></div>
</section>

<!-- Quote -->
<section class="page page--quote">
  <div class="header" role="img" aria-label="Warm orange-tinted photo of a fire extinguisher behind the letterhead"></div>
  <div class="brand" style="left:32px;top:32px;font-size:28px;color:var(--white)"><span class="brand-mark"></span>VOLT3</div>
  <div class="tagline" style="left:32px;top:62px;font-size:4.6px;letter-spacing:2.2px;color:#f3d6c4">PASSIVE FIRE PROTECTION</div>
  <div class="company"><strong>VOLT3 Pty Ltd</strong>4/22 Harlow Street<br>Ferndale VIC 3190<br>ABN: 48 203 615 907<br>admin@volt3.com.au</div>

  <div class="q-head"><span class="c-sl">SL.</span><span class="c-desc">Item Description</span><span class="c-price">Price</span><span class="c-qty">Qty.</span><span class="c-total">Total</span></div>
  <div class="q-body">
    <div class="q-row" style="top:0"><span class="c-sl">1</span><span class="c-desc">Lorem Ipsum Dolor</span><span class="c-price">$50.00</span><span class="c-qty">1</span><span class="c-total">$50.00</span></div>
    <div class="q-row" style="top:40px"><span class="c-sl">2</span><span class="c-desc">Pellentesque id neque ligula</span><span class="c-price">$20.00</span><span class="c-qty">3</span><span class="c-total">$60.00</span></div>
    <div class="q-row" style="top:80px"><span class="c-sl">3</span><span class="c-desc">Interdum et malesuada fames</span><span class="c-price">$10.00</span><span class="c-qty">2</span><span class="c-total">$20.00</span></div>
    <div class="q-row" style="top:120px"><span class="c-sl">4</span><span class="c-desc">Vivamus volutpat faucibus</span><span class="c-price">$90.00</span><span class="c-qty">1</span><span class="c-total">$90.00</span></div>
  </div>

  <div class="abs q-thanks">Thank you for your business</div>
  <div class="abs q-pay">Payment Info:</div>
  <div class="abs q-paylist"><span>Account #:</span><span>1234 5678 9012</span><span>A/C Name:</span><span>Lorem Ipsum</span><span>Bank Details:</span><span>Add your details</span></div>
  <div class="abs q-sum"><span>Sub Total:</span><span>$220.00</span><span>Tax:</span><span>0.00%</span></div>
  <div class="abs q-total"><span>Total:</span><span>$220.00</span></div>
  <div class="abs q-line"></div>
  <div class="abs q-terms">Terms &amp; Conditions</div>
  <div class="abs q-terms-text">Lorem ipsum dolor sit amet, consectetur adipiscing elit. Fusce dignissim pretium consectetur. Curabitur tempor posuere massa in varius. Pellentesque viverra nibh eu vehicula mattis. Nullam porta</div>
  <div class="abs q-sign">Authorised Sign</div>
  <div class="footer">www.volt3.com.au</div>
</section>

<!-- Work docket -->
<section class="page page--docket">
  <div class="header" role="img" aria-label="Warm orange-tinted photo of a fire extinguisher behind the letterhead"></div>
  <div class="brand" style="left:32px;top:32px;font-size:28px;color:var(--white)"><span class="brand-mark"></span>VOLT3</div>
  <div class="tagline" style="left:32px;top:62px;font-size:4.6px;letter-spacing:2.2px;color:#f3d6c4">PASSIVE FIRE PROTECTION</div>
  <div class="company"><strong>VOLT3 Pty Ltd</strong>4/22 Harlow Street<br>Ferndale VIC 3190<br>ABN: 48 203 615 907<br>admin@volt3.com.au</div>

  <div class="d-rule" style="left:20px;width:93px"></div>
  <div class="d-rule" style="left:282px;width:94px"></div>
  <div class="d-pill">WORK DOCKET</div>

  <div class="abs d-client">Brancato Builders 148 Garnet</div>
  <div class="abs d-date" style="left:215px">26th October, 2023</div>
  <div class="abs d-addr">St Port Marlow VIC 3209</div>
  <div class="abs d-contact">Matteo</div>

  <div class="d-info"><b>Work Docket: 1188</b><p>Works completed at <strong>36 Whitlam Street, Ashby Ponds</strong> as directed by <strong>Matteo</strong> of Brancato Builders as listed below.</p></div>

  <div class="d-works"></div>
  <div class="d-works-pill">Works Completed:</div>
  <div class="d-item" style="top:280px">Basement 1 – Fan Room<small>1 x 20mm x 20mm penetration with conduit through blockwork wall (?)</small></div>
  <div class="d-item" style="top:308px">Basement 1 – Apartment 38 Garage<small>2 x 100mm x 100mm penetration with sprinkler pipe &amp; wrap through slab wall (Wet Fire)</small></div>
  <div class="d-item" style="top:336px">Basement 1 – Apartment 34 Garage<small>2 x 100mm x 100mm penetration with sprinkler pipe &amp; wrap through slab wall (Wet Fire)</small></div>
  <div class="d-item" style="top:364px">Basement 1 – Apartment 30 Garage<small>2 x 100mm x 100mm penetration with sprinkler pipe &amp; wrap through slab wall (Wet Fire)</small></div>
  <div class="d-item" style="top:392px">Basement 1 – Apartment 28<small>5mtrs of caulking through slab wall (one side only) (Brickies)</small></div>
  <div class="d-item" style="top:423px">Basement 1 – Apartment 28<small>5mtrs of caulking through slab wall (one side only) (Brickies)</small></div>
  <div class="d-item" style="top:454px">Basement 1 – Back Stairwell<small>1 x 400mm x 400mm penetration empty through blockwork wall (Builder)</small></div>
  <div class="footer">www.volt3.com.au</div>
</section>

<!-- Certificate -->
<section class="page page--cert cert">
  <div class="header" role="img" aria-label="Warm orange-tinted photo of a fire extinguisher behind the letterhead"></div>
  <div class="brand" style="left:32px;top:32px;font-size:28px;color:var(--white)"><span class="brand-mark"></span>VOLT3</div>
  <div class="tagline" style="left:32px;top:62px;font-size:4.6px;letter-spacing:2.2px;color:#f3d6c4;font-family:'Montserrat',sans-serif">PASSIVE FIRE PROTECTION</div>
  <div class="company" style="font-family:'Montserrat',sans-serif"><strong>VOLT3 Pty Ltd</strong>4/22 Harlow Street<br>Ferndale VIC 3190<br>ABN: 48 203 615 907<br>admin@volt3.com.au</div>

  <div class="cert-field" style="top:126px"><span class="label">Client:</span><span>Sentinel Check Pty Ltd</span></div>
  <div class="cert-field" style="top:148px"><span class="label">Job:</span><strong>418 Kellaway Road, Elm Hills</strong></div>
  <div class="cert-field" style="top:169px"><span class="label" style="width:auto;margin-right:5px">Certificate Number:</span><span class="cert-num">2324</span></div>
  <div class="cert-field" style="top:190px"><span class="label">Reference:</span><span style="width:240px;line-height:1.35">Fire/smoke sealing of your various service penetrations as detailed below.</span></div>

  <p class="cert-para" style="top:241px"><strong>VOLT3 Pty. Ltd</strong>. certifies that as part of our contracted works, we have carried out the above fire protection at <strong>418 Kellaway Road, Elm Hills</strong> as instructed by <strong>Lena Vos</strong> of <strong>Sentinel Check Pty Ltd.</strong></p>
  <p class="cert-para" style="top:303px;line-height:1.35">These works have been completed and checked using the approved proprietary fire resistance tested products &amp; systems as <strong>per AS1530 part 4 &amp; AS4072 part 1</strong></p>
  <p class="cert-para" style="top:340px;line-height:1.35">Any works that are modified, damaged, or disturbed following completion are not covered by this certification.</p>
  <p class="cert-para" style="top:380px">Installed in accordance with the manufacturer’s specifications.</p>
  <p class="cert-para" style="top:406px"><span class="label">Signed:</span><span class="sig" role="img" aria-label="Handwritten signature"></span></p>
  <p class="cert-para" style="top:430px"><span class="label">Name:</span> Tomas Reilly</p>
  <p class="cert-para" style="top:451px"><span class="label">Date:</span> 28<sup style="font-size:5px">th</sup> May, 2026</p>
  <div class="footer" style="font-family:'Montserrat',sans-serif">www.volt3.com.au</div>
</section>

</body>
</html>
```